Oven Cleaning Business owner needs business card design

Hi there,
Would like for a business card to be designed for myself, the owner of a professional oven cleaning business on the Sunshine Coast.
Would like it to look sleek, and modern-ish. Bit creative is encouraged too.
Include following:
Name/title: Corin ter Haghe, Owner
Phone number: 1300 482 916
Email: info@hearthshinecrew.com.au
Website: www.hearthshinecrew.com.au

```html
<!DOCTYPE html>
<html lang="en">
<head>
<meta charset="utf-8">
<title>Hearthshine Crew – Business Card</title>
<link rel="stylesheet" href="https://fonts.googleapis.com/css2?family=Montserrat:wght@400;600;700&display=swap">
<style>
  :root {
    --stage: #3d3d3d;
    --card: #121212;
    --teal: #4fc3cc;
    --white: #ffffff;
    --grey: #d6d6d6;
    --font: "Montserrat", Arial, sans-serif;
  }
  * { box-sizing: border-box; margin: 0; padding: 0; }
  html, body {
    width: 1200px; height: 801px; overflow: hidden;
    background: var(--stage);
    font-family: var(--font);
  }
  .sheet {
    position: relative; width: 1200px; height: 801px;
    display: flex; flex-direction: column; align-items: center; justify-content: center; gap: 44px;
  }
  .card {
    position: relative; width: 520px; height: 298px;
    background: var(--card);
    border-bottom: 3px solid var(--teal);
    box-shadow: 0 14px 30px rgba(0,0,0,.35);
  }
  /* front */
  .card--front { display: flex; align-items: center; }
  .brand {
    display: flex; align-items: center; gap: 12px;
    width: 272px; padding-left: 34px;
  }
  .brand__dot {
    flex: none; width: 30px; height: 30px; border-radius: 50%;
    background: var(--teal);
  }
  .brand__name {
    color: var(--white); font-weight: 700; font-size: 21px;
    letter-spacing: .04em; line-height: 1.1; text-transform: uppercase;
  }
  .divider {
    width: 1px; height: 62px; background: var(--teal); opacity: .8;
  }
  .contact { padding-left: 18px; }
  .contact__name {
    color: var(--teal); font-weight: 700; font-size: 17px;
    letter-spacing: -.01em; text-transform: uppercase;
  }
  .contact__title { color: var(--grey); font-size: 12px; margin: 2px 0 8px; }
  .contact__list { list-style: none; }
  .contact__item {
    display: flex; align-items: center; gap: 6px;
    color: var(--white); font-size: 11.5px; line-height: 1.55;
  }
  .contact__icon { width: 10px; height: 10px; fill: var(--teal); flex: none; }
  /* back */
  .card--back { display: flex; align-items: center; justify-content: center; }
  .card--back .brand { width: auto; padding: 0; gap: 14px; }
  .card--back .brand__dot { width: 42px; height: 42px; }
  .card--back .brand__name { font-size: 26px; }
</style>
</head>
<body>
<main class="sheet">
  <section class="card card--front" aria-label="Card front">
    <div class="brand">
      <span class="brand__dot" aria-hidden="true"></span>
      <span class="brand__name">Hearthshine Crew</span>
    </div>
    <span class="divider" aria-hidden="true"></span>
    <div class="contact">
      <h1 class="contact__name">Corin ter Haghe</h1>
      <p class="contact__title">Owner</p>
      <ul class="contact__list">
        <li class="contact__item">
          <svg class="contact__icon" viewBox="0 0 24 24" aria-hidden="true"><path d="M6.6 10.8a15.1 15.1 0 0 0 6.6 6.6l2.2-2.2a1 1 0 0 1 1-.25 11.4 11.4 0 0 0 3.6.57 1 1 0 0 1 1 1V20a1 1 0 0 1-1 1A17 17 0 0 1 3 4a1 1 0 0 1 1-1h3.5a1 1 0 0 1 1 1c0 1.25.2 2.45.57 3.57a1 1 0 0 1-.25 1z"/></svg>
          1300 482 916
        </li>
        <li class="contact__item">
          <svg class="contact__icon" viewBox="0 0 24 24" aria-hidden="true"><path d="M2 5h20v14H2z M3.5 6.5 12 13l8.5-6.5" fill="none" stroke="#4fc3cc" stroke-width="2.4"/></svg>
          info@hearthshinecrew.com.au
        </li>
        <li class="contact__item">
          <svg class="contact__icon" viewBox="0 0 24 24" aria-hidden="true"><g fill="none" stroke="#4fc3cc" stroke-width="2.2"><circle cx="12" cy="12" r="10"/><path d="M2 12h20M12 2c3 3 3 17 0 20M12 2c-3 3-3 17 0 20"/></g></svg>
          www.hearthshinecrew.com.au
        </li>
      </ul>
    </div>
  </section>

  <section class="card card--back" aria-label="Card back">
    <div class="brand">
      <span class="brand__dot" aria-hidden="true"></span>
      <span class="brand__name">Hearthshine Crew</span>
    </div>
  </section>
</main>
</body>
</html>
```